Calendar Infographic Design

I teach and connect Human Resource professionals in the United States. They are almost all women age 35-55. They typically work in small organizations that have less than 100 employees.

We use the attached document as a lead magnet. It is for Human Resources Professionals to keep track of important compliance dates. I'd like it to be more interesting. It can be designed at 8 1/2 X 11 as most people will print it out.

I would like to see more interesting designs that help identify the key deadlines. It should have my branding, but most people know me more than the brand so I am attaching a picture as well for you to consider incorporating - but you do not have to use it.

Target Market(s)

Professional Human Resource Woman Age 55-55

Industry/Entity Type

Human Resources, especially small business

Font styles to use
Sans Serif

Colors
0054AA
0677BA
7BADD7
CADEEF
E8F1F8
FFC000
F8CF3A
FAE287
FDF2CF
FEFAEE
EE7325
F08F49
F5BC92
FAE3D3
FDF4ED

Requirements
Must have
• the dates you see on the current card included and my website www.staffbrightly.net

```html
<!DOCTYPE html>
<html lang="en">
<head>
<meta charset="utf-8">
<title>Calendar of Critical HR Dates</title>
<link rel="stylesheet" href="https://fonts.googleapis.com/css2?family=Archivo+Black&family=Arimo:wght@700&family=Source+Sans+3:wght@400;600&display=swap">
<style>
  :root {
    --title-orange: #E0622A;
    --tab-gold: #F9B214;
    --tab-edge: #E8920E;
    --card-blue: #B7DAFC;
    --navy: #1D4E9A;
    --ink: #1c1c1c;
    --mark-tint: rgba(29, 78, 154, 0.10);
    --photo-tone: #3a8fcf;
  }
  * { box-sizing: border-box; margin: 0; padding: 0; }
  html, body { width: 927px; height: 1200px; overflow: hidden; }
  body {
    position: relative;
    background: linear-gradient(180deg, #fbfbfb 0%, #eeeeef 55%, #e1e1e3 100%);
    font-family: "Source Sans 3", Arial, sans-serif;
    color: var(--ink);
  }
  .page-title {
    position: absolute; left: 102px; top: 80px;
    font-family: "Arimo", Arial, sans-serif; font-weight: 700;
    font-size: 35px; letter-spacing: 0.2px;
    color: var(--title-orange);
  }
  .author-photo {
    position: absolute; left: 783px; top: 40px;
    width: 75px; height: 73px; border-radius: 16px;
    background: radial-gradient(circle at 50% 40%, #c9a38a 0%, #8a6048 40%, var(--photo-tone) 75%);
  }
  .brand-name {
    position: absolute; left: 770px; top: 124px; width: 100px;
    text-align: center;
    font-family: "Source Sans 3", Arial, sans-serif; font-weight: 600;
    font-size: 15px; line-height: 1.05; color: var(--navy);
  }
  .month-grid {
    position: absolute; left: 103px; top: 173px;
    display: grid;
    grid-template-columns: repeat(3, 229px);
    grid-auto-rows: 181px;
    column-gap: 19px; row-gap: 15px;
  }
  .month { position: relative; }
  .month-card {
    position: absolute; left: 5px; top: 5px; width: 224px; height: 176px;
    background: var(--card-blue);
    border: 3px solid #fff; border-radius: 10px;
    box-shadow: 0 1px 3px rgba(0,0,0,0.18);
    padding: 63px 13px 0 12px;
  }
  .month-card.dense { padding-top: 49px; }
  .month-tab {
    position: absolute; left: 0; top: 0; width: 116px; height: 43px;
    background: var(--tab-gold);
    border: 3px solid var(--tab-edge); border-radius: 10px;
    box-shadow: 0 1px 3px rgba(0,0,0,0.25);
    display: flex; align-items: center; justify-content: center;
    font-family: "Archivo Black", "Arial Black", sans-serif;
    font-size: 25px; color: var(--navy); letter-spacing: 0.5px;
    z-index: 1;
  }
  .date-list { list-style: none; font-size: 10.6px; line-height: 12.2px; }
  .date-list li { position: relative; padding-left: 14px; margin-bottom: 8.8px; text-align: justify; min-height: 12.2px; }
  .date-list li::before {
    content: ""; position: absolute; left: 1px; top: 5px;
    width: 2.6px; height: 2.6px; border-radius: 50%; background: var(--ink);
  }
  .dense .date-list { font-size: 8.8px; line-height: 12.7px; }
  .dense .date-list li { margin-bottom: 0; }
  .date-list.tight li { margin-bottom: 0; }
  sup { font-size: 0.6em; line-height: 0; }
  .quiet-mark {
    position: absolute; left: 0; right: 0; top: 66px;
    text-align: center;
    font-family: "Source Sans 3", Arial, sans-serif; font-weight: 600;
    font-size: 30px; line-height: 1; color: var(--mark-tint);
  }
  .annual {
    position: absolute; left: 108px; top: 962px; width: 719px; height: 124px;
    display: flex;
    border: 3px solid #fff; border-radius: 10px; overflow: hidden;
    box-shadow: 0 1px 3px rgba(0,0,0,0.18);
  }
  .annual-label {
    width: 224px; background: var(--tab-gold);
    border: 3px solid var(--tab-edge); border-radius: 10px 0 0 10px;
    display: flex; align-items: center; justify-content: center;
    font-family: "Archivo Black", "Arial Black", sans-serif;
    font-size: 25px; color: var(--navy); letter-spacing: 0.5px;
  }
  .annual-body { flex: 1; background: var(--card-blue); padding: 18px 0 0 7px; }
  .annual-body .date-list { font-size: 10.8px; line-height: 12.2px; }
  .annual-body .date-list li { margin-bottom: 0; padding-left: 14px; text-align: left; }
  .disclaimer {
    position: absolute; left: 56px; top: 1107px; width: 816px;
    font-family: "Arimo", Arial, sans-serif; font-weight: 700;
    font-size: 11.6px; color: #222; letter-spacing: 0.15px; white-space: nowrap;
  }
  .footer-line {
    position: absolute; left: 56px; top: 1131px; width: 815px;
    display: flex; justify-content: space-between;
    font-family: "Arimo", Arial, sans-serif; font-weight: 700;
    font-size: 11.6px; color: #222;
  }
</style>
</head>
<body>
  <h1 class="page-title">CALENDAR OF CRITICAL HR DATES</h1>
  <div class="author-photo" role="img" aria-label="Portrait photo of the Staff Brightly founder"></div>
  <div class="brand-name">Staff Brightly</div>

  <main class="month-grid">
    <section class="month">
      <div class="month-tab">JAN</div>
      <div class="month-card dense">
        <ul class="date-list">
          <li>Prepare OSHA 300A</li>
          <li>Gather Data for 5500 reporting; check with broker on requirement</li>
          <li>Advise employees of increase allowed in retirement plan, HSA, dependent care and flexible spending accounts if allowed by law</li>
          <li>Send W2s and 1099s as appropriate</li>
          <li>Be sure to change benefit deductions in payroll</li>
          <li>Download new W4 with current year for new hires</li>
        </ul>
      </div>
    </section>
    <section class="month">
      <div class="month-tab">FEB</div>
      <div class="month-card">
        <ul class="date-list">
          <li>February 1<sup>st</sup> – Post OSHA 300A log</li>
          <li>Consider total compensation statements for previous year</li>
          <li>Black History Month</li>
        </ul>
      </div>
    </section>
    <section class="month">
      <div class="month-tab">MAR</div>
      <div class="month-card">
        <ul class="date-list">
          <li>March 1<sup>st</sup>– Medicare Part D reporting due</li>
          <li>First Friday – National Employee Appreciation day</li>
          <li>EEO-1 (over 100 employees) and VETS 4212 (federal contractors) reports due</li>
        </ul>
      </div>
    </section>

    <section class="month">
      <div class="month-tab">APR</div>
      <div class="month-card">
        <ul class="date-list">
          <li>April 1<sup>st</sup> – H-1B filing begins</li>
          <li>April 30<sup>th</sup> – Take down OSHA 300A and retain for 5 years</li>
        </ul>
      </div>
    </section>
    <section class="month">
      <div class="month-tab">MAY</div>
      <div class="month-card"><div class="quiet-mark" aria-hidden="true">Staff Brightly</div></div>
    </section>
    <section class="month">
      <div class="month-tab">JUN</div>
      <div class="month-card"><div class="quiet-mark" aria-hidden="true">Staff Brightly</div></div>
    </section>

    <section class="month">
      <div class="month-tab">JUL</div>
      <div class="month-card">
        <ul class="date-list">
          <li>File 5500 for Retirement plan and other benefits if required</li>
        </ul>
      </div>
    </section>
    <section class="month">
      <div class="month-tab">AUG</div>
      <div class="month-card">
        <ul class="date-list">
          <li>Send Summary Plan Description of retirement plan if required</li>
        </ul>
      </div>
    </section>
    <section class="month">
      <div class="month-tab">SEP</div>
      <div class="month-card">
        <ul class="date-list">
          <li>Consider your holiday schedule for payroll and time off and publish to employees</li>
        </ul>
      </div>
    </section>

    <section class="month">
      <div class="month-tab">OCT</div>
      <div class="month-card">
        <ul class="date-list">
          <li>Medicare Part D credible coverage notices to employees</li>
          <li>October 16 – National Boss' Day</li>
        </ul>
      </div>
    </section>
    <section class="month">
      <div class="month-tab">NOV</div>
      <div class="month-card">
        <ul class="date-list tight">
          <li>Receipt of unemployment rate – verify accuracy</li>
          <li aria-hidden="true"></li>
          <li>Remind employees to use FSA dollars</li>
        </ul>
      </div>
    </section>
    <section class="month">
      <div class="month-tab">DEC</div>
      <div class="month-card">
        <ul class="date-list">
          <li>Calculate imputed income for life insurance, personal use of auto, etc.</li>
          <li>Subchapter S corps: Calculate tax implications and reimburse accordingly</li>
        </ul>
      </div>
    </section>
  </main>

  <section class="annual">
    <div class="annual-label">ANNUALLY</div>
    <div class="annual-body">
      <ul class="date-list">
        <li>Review employee handbook for necessary updates</li>
        <li>Determine if your current employment posters are up to date</li>
        <li>Remove all I-9's for terminated employees that are no longer required</li>
        <li>Communicate with employees regarding lack of tolerance for harassment and discrimination</li>
        <li>Complete HR Audit provided as part of People Playbook</li>
      </ul>
    </div>
  </section>

  <p class="disclaimer">Each organization will have specific deadlines based on size, industry and location.&nbsp; This is not all inclusive or to be taken as legal advice.</p>
  <div class="footer-line"><span>©Staff Brightly</span><span>www.staffbrightly.net</span></div>
</body>
</html>
```